Presentation card Venture KELO - Tech Incubator from Perú

We need a Design to promote the incubator of technology Startups.
We are in Perú, we work with a string tech filter and develop enterprenurship competencies in the Startup team.
The card is to facilitators and staff memebers of VentureKELO.
We want a clear, modern, tech and agile Design.

We work to help New enterprises of technology here in Perú, we expect the candidates have a big competencies to Research and develop technological products.

We work using methodologies from QRB, Folmestry, Brakewell and Harrowgate univeesities. Our book base is the disciplina of enterpreneur.

We work events all year using diferent formats: Brightforge, Vorne price, OPRA Model Competition you can use these logros in your Design.

Set the name, role, email, cell phone number, address.

Example:
// Contact info section
Tobías Quiroveda
Swift Modeling Hub Manager
tobias.quiroveda@kelo-example.pe
(511) 999 000 417

// Address info section
VentureKELO
Technology-based business incubator
Av. Los Cedrales 884, Valdora
Lima - Perú
web: venture-kelo-example.org.pe
email: venture@kelo-example.pe
phone number: (511) 3926508 ext. 4418

// (optional)Lema section
Making happy using technology

// Social network section
facebook: venturekelooficial

Target Market(s)

Enterprenurship, CTO, Investors, Companies interested on open innovation services

Industry/Entity Type

Information Technology

Contact Information for Business Card

Name, Role, Email, Cell phone number

Colors

Designer to choose colors to be used in the design.

Requirements
Must have
• Logo forms and colors
Nice to have
• I add pictures of the leaders of incubator
Should not have
• No vertical designs

```html
<!DOCTYPE html>
<html lang="es">
<head>
<meta charset="utf-8">
<title>Venture KELO – Business Card</title>
<link rel="stylesheet" href="https://fonts.googleapis.com/css2?family=Arimo:wght@400;700&display=swap">
<style>
  :root {
    --backdrop: #e4e4e4;
    --card-white: #fbfbfb;
    --brand-yellow: #e8b21a;
    --brand-crimson: #d9234f;
    --ink: #1c1c1c;
    --photo-dark: #2a3140;
    --photo-mid: #5d7a4e;
    --photo-light: #c9ccc6;
  }
  * { box-sizing: border-box; margin: 0; padding: 0; }
  html, body {
    width: 1200px;
    height: 864px;
    overflow: hidden;
    background: var(--backdrop);
    font-family: "Arimo", Arial, sans-serif;
  }
  .card-sheet {
    position: relative;
    width: 1200px;
    height: 864px;
    display: flex;
    align-items: center;
    justify-content: center;
    gap: 40px;
  }
  .card {
    width: 540px;
    height: 309px;
    border-radius: 4px;
    overflow: hidden;
    box-shadow: 0 6px 18px rgba(0,0,0,0.18);
    position: relative;
  }
  .card-front {
    background: var(--card-white);
    display: flex;
    flex-direction: column;
    align-items: center;
    justify-content: center;
    text-align: center;
  }
  .brand-mark {
    display: flex;
    align-items: center;
    gap: 10px;
    font-weight: 700;
    color: var(--ink);
    letter-spacing: -0.5px;
  }
  .brand-mark .brand-square {
    width: 16px;
    height: 16px;
    background: var(--brand-crimson);
  }
  .card-front .brand-mark { font-size: 38px; margin-bottom: 28px; }
  .contact-name {
    font-size: 21px;
    font-weight: 700;
    color: var(--ink);
  }
  .contact-role {
    font-size: 17px;
    color: var(--brand-crimson);
    margin-top: 3px;
    margin-bottom: 16px;
  }
  .contact-line {
    font-size: 15px;
    color: var(--ink);
    line-height: 1.45;
  }
  .card-back {
    background: var(--brand-yellow);
    display: flex;
    flex-direction: column;
  }
  .team-photo {
    height: 44%;
    background: linear-gradient(100deg, var(--photo-light) 0%, var(--photo-dark) 22%, var(--photo-mid) 45%, var(--photo-dark) 70%, var(--photo-light) 100%);
  }
  .back-brand {
    flex: 1;
    display: flex;
    align-items: center;
    justify-content: center;
    padding-bottom: 30px;
  }
  .card-back .brand-mark { font-size: 34px; }
</style>
</head>
<body>
  <main class="card-sheet">
    <section class="card card-front">
      <div class="brand-mark"><span class="brand-square"></span><span>Venture KELO</span></div>
      <p class="contact-name">Tobías Quiroveda</p>
      <p class="contact-role">Senior Software Development Engineer</p>
      <p class="contact-line">+00 410 000 2871</p>
      <p class="contact-line">tobias@kelo-example.pe</p>
    </section>
    <section class="card card-back">
      <div class="team-photo" role="img" aria-label="Group photo of the incubator team standing together in an office"></div>
      <div class="back-brand">
        <div class="brand-mark"><span class="brand-square"></span><span>Venture KELO</span></div>
      </div>
    </section>
  </main>
</body>
</html>
```